Mirela Hastow ADHD coach needs a flyer

I need a flyer to be sent by email. the copy is attached. It can be changed/reduced to fit the flyer. I would like to keep my website colors. My website is www.mirelahastow.example - Thank you!

```html
<!DOCTYPE html>
<html lang="en">
<head>
<meta charset="utf-8">
<title>Mirela Hastow – Empowering Focus</title>
<link href="https://fonts.googleapis.com/css2?family=Roboto+Condensed:ital,wght@0,300;0,400;0,700;1,700&display=swap" rel="stylesheet">
<style>
:root{
  --backdrop:#878a95;
  --steel:#9bb5c1;
  --steel-dark:#6f8d9c;
  --mist:#d2dbe0;
  --mist-2:#c6d3d9;
  --bubble:#dfe7eb;
  --ink:#3f5d72;
  --ink-soft:#4f6878;
  --title:#5a7b8d;
  --white:#ffffff;
  --pill:#3f5d72;
}
*{margin:0;padding:0;box-sizing:border-box}
html,body{width:1200px;height:1200px;overflow:hidden}
body{background:var(--backdrop);font-family:"Roboto Condensed",Arial,sans-serif;color:var(--ink);position:relative}
.flyer{position:absolute;left:312px;top:33px;width:590px;height:1127px;background:var(--mist);overflow:hidden}
.abs{position:absolute}

.brand-panel{left:0;top:0;width:215px;height:238px;background:var(--steel)}
.brand-name{left:14px;top:17px;width:186px;height:31px;background:var(--steel-dark);border:2px solid #dbe5ea;color:var(--white);font-size:20px;display:flex;align-items:center;justify-content:center;letter-spacing:.2px}
.tagline{left:0;top:78px;width:215px;text-align:center;color:var(--white);font-size:22px;font-weight:300}
.chevrons{left:56px;top:117px}

.headline{left:215px;top:0;width:375px;height:110px;background:var(--white);text-align:center;color:var(--title)}
.headline h1{font-size:27px;font-weight:700;margin-top:17px;line-height:30px}
.headline p{font-size:19.5px;line-height:24px;font-weight:400}

.photo-group{left:87px;top:110px;width:503px;height:160px;background:linear-gradient(180deg,#b9d39a 0%,#8fb07a 40%,#6c87a4 75%,#8a6f58 100%)}
.photo-coach{left:1px;top:328px;width:201px;height:132px;background:linear-gradient(90deg,#bfcbd0,#c7d2d6 60%,#c2ccd0)}

.helps-title{left:10px;top:297px;font-size:20px;color:var(--ink);font-weight:400;white-space:nowrap}
.helps-text{left:21px;top:471px;width:180px;font-size:10.6px;line-height:12px;color:var(--ink-soft);text-align:justify}
.helps-text p{margin-bottom:12px}
.helps-list{list-style:none}
.helps-list li{position:relative;margin-bottom:5px;text-align:justify}
.helps-list li::before{content:"";position:absolute;left:-13px;top:1px;width:9px;height:9px;border:1px solid var(--ink-soft);border-radius:50%}

.story{left:215px;top:285px;width:375px;height:527px;background:var(--white)}
.story-lead{left:15px;top:13px;width:343px;font-size:10.8px;line-height:12px;font-weight:700;font-style:italic;color:var(--ink);text-align:justify;padding-bottom:6px;border-bottom:1px solid var(--steel)}
.story-body{left:15px;top:55px;width:343px;font-size:10.6px;line-height:12px;color:var(--ink-soft);text-align:justify}
.story-body p{margin-bottom:12px}

.potential{left:14px;top:269px;width:361px;height:123px;background:var(--steel);color:var(--white);text-align:center}
.potential h2{font-size:21px;font-weight:400;margin-top:5px;line-height:24px}
.potential h3{font-size:17px;font-weight:400;text-decoration:underline;text-underline-offset:3px;line-height:22px}
.potential ul{list-style:none;text-align:left;margin:8px 0 0 70px;font-size:10.6px;line-height:12px}
.potential li::before{content:"• "}

.have-title{left:0;top:406px;width:375px;text-align:center;font-size:23px;font-weight:400;color:var(--ink)}
.benefits{left:16px;top:440px;width:345px;height:68px}
.benefit{position:absolute;font-size:10.6px;line-height:13px;color:var(--ink-soft)}
.tick{position:absolute}

.voice{top:812px;height:205px;width:295px}
.voice-parents{left:0;background:var(--steel)}
.voice-students{left:295px;background:var(--mist-2)}
.bubble-label{font-size:19px;line-height:20px;font-weight:400;white-space:nowrap}
.voice-parents .bubble-label{color:var(--ink)}
.voice-students .bubble-label{color:var(--white)}
.avatar{border-radius:50%;border:3px solid var(--white);box-shadow:0 0 0 1px #9aa9b1}
.quote{font-size:10.3px;line-height:13px}
.quote p{margin-bottom:12px}
.voice-parents .quote{color:var(--white);text-align:justify}
.voice-students .quote{color:var(--ink-soft)}

.next{left:0;top:1017px;width:590px;height:30px;background:var(--white);text-align:center;font-size:19.5px;line-height:30px;color:var(--ink)}
.contact{left:0;top:1047px;width:590px;height:80px;background:var(--steel);text-align:center;color:var(--ink-soft)}
.contact .lead{font-size:14px;margin-top:7px;line-height:16px}
.contact .row{margin-top:6px;font-size:14px;display:flex;justify-content:center;align-items:center;gap:6px}
.pill{display:inline-flex;align-items:center;gap:5px;background:var(--pill);color:var(--white);border:1.5px solid #dbe5ea;border-radius:12px;height:23px;padding:0 9px;font-size:14px}
</style>
</head>
<body>
<div class="flyer">

  <div class="abs brand-panel"></div>
  <div class="abs brand-name">• MIRELA HASTOW •</div>
  <div class="abs tagline">EMPOWERING FOCUS</div>
  <svg class="abs chevrons" width="20" height="106" viewBox="0 0 20 106" fill="none" stroke="#ffffff" stroke-width="1.5">
    <path d="M2 2l8 7 8-7M2 8l8 7 8-7"/>
    <path d="M2 24l8 7 8-7M2 30l8 7 8-7"/>
    <path d="M2 46l8 7 8-7M2 52l8 7 8-7"/>
    <path d="M2 68l8 7 8-7M2 74l8 7 8-7"/>
    <path d="M2 90l8 7 8-7M2 96l8 7 8-7"/>
  </svg>

  <div class="abs headline">
    <h1>HELPING YOUR CHILD</h1>
    <p>with ADHD or Other Learning Challenges</p>
    <p>Thrive in College and Beyond</p>
  </div>

  <div class="abs photo-group" role="img" aria-label="Photo of a group of smiling college students sitting together outdoors with laptops and tablets"></div>

  <div class="abs helps-title">»» HOW MIRELA HELPS</div>
  <div class="abs photo-coach" role="img" aria-label="Portrait photo of coach Mirela Hastow in a light jacket"></div>

  <div class="abs helps-text">
    <p>Mirela has taken students from failing to a 3.0 GPA, and from a C student to the Dean’s List, in just one semester. It doesn’t take years to provide lasting results; all it takes is the right guide.</p>
    <p>Uniquely positioned to help your child, Mirela:</p>
    <ul class="helps-list">
      <li>Tailors support so that your child improves focus and maximizes their potential in college and beyond.</li>
      <li>Understands your child’s unique needs - she sees the gifts that others often miss.</li>
      <li>Knows the academic landscape intimately, including the challenges faced by students with ADHD and other conditions.</li>
      <li>Helps with the logistics of scheduling in a way that most advisors can’t, enrolling students in the courses that best suit their learning style.</li>
      <li>Nurtures the brilliance in your bright child.</li>
      <li>Provides a balance between encouraging</li>
    </ul>
  </div>

  <div class="abs story">
    <div class="abs story-lead">Academic success coaching that leads to lifelong transformation for students with ADHD and similar challenges that may have impeded their ability to thrive.</div>
    <div class="abs story-body">
      <p>Sending your child off to college can feel scary, especially if that college is hundreds of miles away. You worry about how they’ll do on their own—whether they’ll make friends, earn good grades, and be happy—especially without you there to support them daily. You know your child is bright, and you want them to have a great future, but you’re concerned they will struggle without the right support and resources.</p>
      <p>You don’t need to feel helpless as you send your child off to this next stage of their lives. Mirela is dedicated to making that transition easier for everyone. Mirela Hastow has years of experience helping students thrive despite their challenges. She sees your child’s potential and helps them see it, too. She provides a safety net as they adjust to a new environment at college. Her services are comprehensive and adaptable, based on the requirements of each individual: helping with course selection and scheduling, time management, study strategies, focus, making new friends, and adapting to change. Through it all, Mirela guides students through fundamental work on mindset to ensure that changes stick.</p>
    </div>

    <div class="abs potential">
      <h2>REALIZING POTENTIAL</h2>
      <h3>The Transformation You’ll See in Your Child</h3>
      <ul>
        <li>A mindset of self-belief and increased confidence.</li>
        <li>Higher grades and the drive to graduate.</li>
        <li>Social integration and making friends.</li>
        <li>Happiness and fulfillment.</li>
        <li>A deep sense of personal achievement and pride.</li>
      </ul>
    </div>

    <div class="abs have-title">YOU WILL HAVE:</div>
    <div class="abs benefits">
      <svg class="tick" style="left:0;top:0" width="345" height="68" viewBox="0 0 345 68" fill="none">
        <line x1="0" y1="33" x2="345" y2="33" stroke="#9bb5c1" stroke-width="1"/>
        <line x1="174" y1="0" x2="174" y2="66" stroke="#9bb5c1" stroke-width="1"/>
        <g stroke="#7e9cab" stroke-width="1.6">
          <rect x="18" y="10" width="15" height="15"/><path d="M21 16l5 6 10-14" stroke-width="2.6"/>
          <rect x="310" y="10" width="15" height="15"/><path d="M313 16l5 6 10-14" stroke-width="2.6"/>
          <rect x="18" y="44" width="15" height="15"/><path d="M21 50l5 6 10-14" stroke-width="2.6"/>
          <rect x="309" y="44" width="15" height="15"/><path d="M312 50l5 6 10-14" stroke-width="2.6"/>
        </g>
      </svg>
      <div class="benefit" style="left:43px;top:3px">Less stress, knowing that<br>your child is in good hands.</div>
      <div class="benefit" style="left:188px;top:3px">Fewer sleepless nights<br>worrying about your child.</div>
      <div class="benefit" style="left:43px;top:39px">Confidence that they are<br>receiving the right support.</div>
      <div class="benefit" style="left:188px;top:39px">Joy and pride at<br>seeing them do well.</div>
    </div>
  </div>

  <div class="abs voice voice-parents">
    <svg class="abs" style="left:48px;top:21px" width="228" height="72" viewBox="0 0 228 72">
      <path d="M0 0H227V52H219L222 70L196 52H0Z" fill="#dfe7eb"/>
      <g transform="translate(18 0)">
        <path d="M186 8q-6 3-6 10h5v8h-8v-8q0-8 8-12zM198 8q-6 3-6 10h5v8h-8v-8q0-8 8-12z" fill="#5a7b8d"/>
      </g>
    </svg>
    <div class="abs avatar" style="left:15px;top:7px;width:76px;height:76px;background:linear-gradient(135deg,#9fb8c4,#6f8897 60%,#c2a48a)" role="img" aria-label="Photo of a smiling parent couple"></div>
    <div class="abs bubble-label" style="left:105px;top:27px">WHAT<br>PARENTS SAY</div>
    <div class="abs quote" style="left:21px;top:104px;width:255px">
      <p>“Mirela was the glue that kept our daughter in college... as our daughter’s Academic Coach, [she] gave our daughter the ability to finish strong by empowering her with the skills needed to be successful.” —Corinne</p>
      <p>“Mirela has always told my daughter not that she can succeed, but that she will succeed.” —Dana</p>
    </div>
  </div>

  <div class="abs voice voice-students">
    <svg class="abs" style="left:18px;top:21px" width="200" height="72" viewBox="0 0 200 72">
      <path d="M0 0H199V52H32L10 70L12 52H0Z" fill="#9bb5c1"/>
      <path d="M20 8q-6 3-6 10h5v8h-8v-8q0-8 8-12zM32 8q-6 3-6 10h5v8h-8v-8q0-8 8-12z" fill="#ffffff"/>
    </svg>
    <div class="abs avatar" style="left:203px;top:7px;width:76px;height:76px;background:linear-gradient(135deg,#d9c7a8,#b99a7b 55%,#47505a)" role="img" aria-label="Photo of two smiling students"></div>
    <div class="abs bubble-label" style="left:66px;top:27px">WHAT<br>STUDENTS SAY</div>
    <div class="abs quote" style="left:18px;top:99px;width:262px">
      <p>“Last semester I completed all 16 hours and I had the highest GPA I’ve ever had!” —Former student</p>
      <p>“Under her instruction, my grades began to improve. I ended up making the Dean’s List during my time at Ridgefield, and I was also inducted into Alder Honor Society. I am currently in my first year of law school at Hollowmere University, a top tier school. ”—Former student</p>
    </div>
  </div>

  <div class="abs next">NEXT STEPS</div>
  <div class="abs contact">
    <p class="lead">To learn more and discuss your child’s individual needs,</p>
    <div class="row">
      <span>call</span>
      <span class="pill">
        <svg width="12" height="12" viewBox="0 0 24 24" fill="#ffffff"><path d="M6.6 10.8a15 15 0 006.6 6.6l2.2-2.2a1 1 0 011-.25 11.4 11.4 0 003.6.57 1 1 0 011 1V20a1 1 0 01-1 1A17 17 0 013 4a1 1 0 011-1h3.5a1 1 0 011 1c0 1.25.2 2.45.57 3.57a1 1 0 01-.25 1z"/></svg>
        555-014-2290
      </span>
      <span>or email</span>
      <span class="pill">
        <svg width="13" height="10" viewBox="0 0 13 10" fill="none" stroke="#ffffff" stroke-width="1.2"><rect x=".6" y=".6" width="11.8" height="8.8"/><path d="M.6.6l5.9 5 5.9-5"/></svg>
        coach@mirelahastow.example
      </span>
    </div>
  </div>

</div>
</body>
</html>
```